Website: mentorprogram for refugees; Uplift your tomorrow

We need a website for our project Kindlo, which mainly will serve as a information site for our stakeholders. (refugees/mentees, employers/mentors, municipality and sponsors)

We also need a logo/visual design program for the project. We are thinking something green/grey/blue - close to the logo used today. The design should communicate growth, understanding/integration, knowledge. The name Kindlo comes from refugees reframing/redesigning their future as part of the concept.

Kindlo is a two-dimensional consept/program to support refugees in redesigning their future and increasing their employability. The program offers a mentor to each refugee. Mentors will be trained in the mentor-role and will be instrumental in supporting the refugees in their quest to understand work culture in Norway. Understanding of intercultural communication and the value of diversity in the workplace is an important part of the program for both parties. Nature will provide a setting for the conversations between mentor and mentee

Logo Text

Kindlo

Number of Pages Required

1 page

Font styles to use
Sans Serif

Colors
9bcb3c
0355a3
f78f20

```html
<!DOCTYPE html>
<html lang="en">
<head>
<meta charset="utf-8">
<title>Kindlo Norway</title>
<link href="https://fonts.googleapis.com/css2?family=Raleway:wght@400;500;600;700&family=Open+Sans:wght@400;600&display=swap" rel="stylesheet">
<style>
:root{
  --green:#3dab6c;
  --dark:#464646;
  --ink:#333;
  --muted:#555;
  --light:#e6e6e6;
  --white:#fff;
  --accent-red:#d9534f;
}
*{box-sizing:border-box;margin:0;padding:0}
html,body{width:1200px;height:2542px;overflow:hidden}
body{position:relative;background:var(--white);font-family:"Open Sans",sans-serif;color:var(--ink)}
.abs{position:absolute}

/* header */
.site-header{left:0;top:0;width:1200px;height:115px;background:var(--white)}
.brand{left:88px;top:24px;display:flex;align-items:center;gap:16px}
.brand-name{font-family:"Raleway",sans-serif;font-weight:500;font-size:34px;line-height:34px;letter-spacing:3px;color:#666}
.brand-mark{width:30px;height:30px;background:var(--green)}
.main-nav{left:480px;top:44px;display:flex;gap:0}
.main-nav a{font-family:"Raleway",sans-serif;font-size:15px;color:var(--ink);text-decoration:none;margin-right:34px}
.btn{display:inline-block;background:var(--green);color:var(--white);font-family:"Raleway",sans-serif;text-decoration:none;border-radius:20px;text-align:center}
.nav-join{left:1003px;top:41px;width:110px;height:37px;line-height:37px;font-size:15px}

/* hero */
.hero{left:0;top:115px;width:1200px;height:478px;background:linear-gradient(180deg,#5d5a55 0%,#3f3c38 55%,#4a4641 100%)}
.hero-title{left:0;top:142px;width:1200px;text-align:center;font-family:"Raleway",sans-serif;font-weight:700;font-size:55px;line-height:67px;color:var(--white)}
.hero-join{left:545px;top:285px;width:110px;height:37px;line-height:37px;font-size:15px}
.hero-arrow{top:238px;width:28px;height:28px}

/* section titles */
.section-title{left:0;width:1200px;text-align:center;font-family:"Raleway",sans-serif;font-weight:500;font-size:32px;color:var(--ink)}
.section-title span{color:var(--green)}
.title-rule{left:540px;width:120px;height:3px;background:var(--ink)}

.about-lead{left:0;top:749px;width:1200px;text-align:center;font-size:14px;line-height:23px;color:var(--muted)}
.feature{top:827px;height:124px;display:flex;align-items:center;color:var(--white);font-family:"Raleway",sans-serif;font-weight:500;font-size:14px;line-height:23px;letter-spacing:.3px}
.feature-dark{left:88px;width:515px;background:var(--dark);clip-path:polygon(0 0,100% 0,96% 100%,0 100%);padding-left:24px}
.feature-green{left:598px;width:515px;background:var(--green);clip-path:polygon(4% 0,100% 0,100% 100%,0 100%);padding-left:26px}
.num{flex:none;width:42px;height:42px;border-radius:50%;background:var(--white);color:var(--ink);font-size:14px;line-height:42px;text-align:center;margin-right:20px}
.feature-green .num{margin-left:0}

/* topics */
.topics{left:0;top:1041px;width:1200px;height:478px;background:linear-gradient(90deg,#2e2c28 0%,#3a3732 45%,#2a2824 100%)}
.topics .section-title{color:var(--white)}
.topic-list{list-style:none;font-size:13px;line-height:26.5px}
.topic-list li::before{content:"\2714";margin-right:6px}
.topics-left{left:180px;top:1184px;width:401px;text-align:right;color:var(--green)}
.topics-left li::before{color:var(--green)}
.topics-right{left:617px;top:1184px;width:460px;color:var(--white)}

/* program */
.program-lead{left:0;top:1683px;width:1200px;text-align:center;font-size:14px;color:var(--ink)}
.program-card{top:1760px;height:245px;color:var(--white);text-align:center;padding:40px 45px 0}
.program-card h3{font-family:"Raleway",sans-serif;font-weight:600;font-size:18px;margin-bottom:12px;letter-spacing:.3px}
.program-card p{font-size:13px;line-height:22.5px}
.card-green{left:88px;width:515px;background:var(--green);clip-path:polygon(0 0,100% 0,97% 100%,0 100%)}
.card-dark{left:598px;width:515px;background:var(--dark);clip-path:polygon(3% 0,100% 0,100% 100%,0 100%)}
.card-badge{top:1738px;width:43px;height:43px;border-radius:50%;color:var(--white);text-align:center;line-height:43px;font-size:14px}
.badge-dark{left:102px;background:var(--dark)}
.badge-green{left:612px;background:var(--green)}
.hl{color:var(--accent-red)}

/* contact bar */
.contact-bar{left:0;top:2105px;width:1200px;height:92px;background:var(--green);color:var(--white);font-size:18px}
.contact-item{top:0;height:92px;display:flex;align-items:center;gap:12px}
.contact-sep{top:24px;width:1px;height:44px;background:rgba(255,255,255,.45)}

/* footer */
.site-footer{left:0;top:2197px;width:1200px;height:345px;background:var(--light)}
.partner-circle{left:88px;top:2272px;width:116px;height:116px;border-radius:50%;border:3px solid #4a5fa0}
.partner-square{left:250px;top:2256px;width:113px;height:150px;background:#9aa89e}
.footer-heading{font-family:"Raleway",sans-serif;font-size:22px;color:var(--ink)}
.field{left:527px;width:256px;height:46px;background:var(--white);border:1px solid #ddd;font-size:12px;padding:15px 28px;color:var(--ink)}
.subscribe{left:527px;top:2395px;width:256px;height:50px;line-height:50px;font-size:22px}
.sitemap{top:2285px;list-style:none;font-size:11.5px;line-height:26px;color:#777}
.footer-rule{left:88px;top:2476px;width:1025px;height:1px;background:#ccc}
.copyright{left:88px;top:2500px;font-size:11.5px;color:#555}
.social{top:2500px;width:16px;height:16px;border-radius:50%;background:#555}
</style>
</head>
<body>

<header class="site-header abs">
  <div class="brand abs"><span class="brand-name">Kindlo<br>Norway</span><span class="brand-mark"></span></div>
  <nav class="main-nav abs">
    <a href="#">Home</a><a href="#">About</a><a href="#">Services</a><a href="#">Program</a><a href="#">Support</a><a href="#">Contact US</a>
  </nav>
  <a class="btn nav-join abs" href="#">Join Us</a>
</header>

<section class="hero abs" role="img" aria-label="Photo of a woman carrying a large woven basket on a rocky path">
  <h1 class="hero-title abs">WELCOME TO<br>KINDLO NORWAY</h1>
  <a class="btn hero-join abs" href="#">Join Us</a>
  <svg class="hero-arrow abs" style="left:30px" viewBox="0 0 28 28"><circle cx="14" cy="14" r="14" fill="#fff"/><path d="M16.5 8 L10.5 14 L16.5 20" stroke="#333" stroke-width="3" fill="none"/></svg>
  <svg class="hero-arrow abs" style="left:1137px" viewBox="0 0 28 28"><circle cx="14" cy="14" r="14" fill="#fff"/><path d="M11.5 8 L17.5 14 L11.5 20" stroke="#333" stroke-width="3" fill="none"/></svg>
</section>

<h2 class="section-title abs" style="top:660px">ABOUT <span>KINDLO NORWAY</span></h2>
<div class="title-rule abs" style="top:713px"></div>
<p class="about-lead abs">A two-dimensional consept to support refugees in redesigning their future and increasing their employability.<br>The program offers a mentor to each refugee. Mentors will be trained in the mentor-role</p>

<div class="feature feature-dark abs"><span class="num">01</span><span>A PROGRAM FOR REFUGEES PROVIDING SUPPORT FOR<br>REFRAMING WORK-LIFE IN A NEW CONTEXT</span></div>
<div class="feature feature-green abs"><span class="num">02</span><span>A MENTOR PROGRAM FOR LEADERS/ PROFESSIONALS<br>ACTING AS MENTORS FOR REFUGEES</span></div>

<section class="topics abs" role="img" aria-label="Dark photo of a man working the ground beside a hut">
  <h2 class="section-title abs" style="top:56px">TOPICS <span>COVERED</span></h2>
  <div class="title-rule abs" style="top:109px;background:#fff"></div>
</section>
<ul class="topic-list topics-left abs">
  <li>Identity in a new context</li>
  <li>Self management</li>
  <li>How to build social capital</li>
  <li>Mindset – sitting in the 'driver's seat'</li>
  <li>Intercultural conflict resolution</li>
  <li>Resilience-training; dealing with rejection</li>
  <li>Trust in a Norwegian context</li>
  <li>Psychological contracts in Norwegian worklife</li>
  <li>How does masculinity &amp; femininity change in a new context</li>
</ul>
<ul class="topic-list topics-right abs">
  <li>Training for mentoring skills</li>
  <li>Understanding organizational diversity</li>
  <li>Building trust in a diverse culture</li>
  <li>Understanding of basic&nbsp; Norwegian work- and leadership styles</li>
  <li>Understanding the basics of post-traumatic stress disorder</li>
  <li>Intercultural conflict resolution</li>
  <li>Bringing learning back to my organization</li>
</ul>

<h2 class="section-title abs" style="top:1593px">PROGRAM <span>INNHOLD</span></h2>
<div class="title-rule abs" style="top:1645px"></div>
<p class="program-lead abs">Kindlo Norway består av to programmer som har noe overlapp</p>

<div class="program-card card-green abs">
  <h3>SELV-LEDELSES PROGRAM FOR FLYKTNINGER</h3>
  <p>Et 5-7 modulers program over 1 år (á 2-3 dager) med stor grad av individuell tilpasning. Det overordnede programmet tilpasses den enkelte kommune basert på deres eksisterende integreringsarbeid</p>
</div>
<div class="program-card card-dark abs">
  <h3>KINDLO MENTORPROGRAM</h3>
  <p>Et 3-4 modulers program der ledere/fagpersoner fra lokale organisasjoner (privat eller offentlig sektor) etter avtale med sin arbeidsgiver stiller som mentor for en flyktning. Disse mentorene vil få et grundig mentor-treningsprogram som også kan anvendes i <span class="hl">de</span> organisasjonen de jobber til daglig Det forventes at mentorene bruker <span class="hl">4-6</span> arbeidsdager <span class="hl">ila ¼ år</span> og noe av sin fritid som mentor for en flyktning</p>
</div>
<div class="card-badge badge-dark abs">01</div>
<div class="card-badge badge-green abs">02</div>

<section class="contact-bar abs">
  <div class="contact-item abs" style="left:210px">
    <svg width="12" height="17" viewBox="0 0 12 17"><path d="M6 0C2.7 0 0 2.6 0 5.9 0 10.3 6 17 6 17s6-6.7 6-11.1C12 2.6 9.3 0 6 0zm0 8.3A2.4 2.4 0 1 1 6 3.5a2.4 2.4 0 0 1 0 4.8z" fill="#fff"/></svg>
    <span>Lindeveien 12, BRØNDAL, 1490.</span>
  </div>
  <div class="contact-sep abs" style="left:572px"></div>
  <div class="contact-item abs" style="left:616px">
    <svg width="15" height="15" viewBox="0 0 24 24"><path d="M6.6 10.8a15.1 15.1 0 0 0 6.6 6.6l2.2-2.2c.3-.3.7-.4 1-.2 1.1.4 2.3.6 3.6.6.6 0 1 .4 1 1V20c0 .6-.4 1-1 1A17 17 0 0 1 3 4c0-.6.4-1 1-1h3.5c.6 0 1 .4 1 1 0 1.3.2 2.5.6 3.6.1.3 0 .7-.2 1z" fill="#fff"/></svg>
    <span>412 00 987</span>
  </div>
  <div class="contact-sep abs" style="left:775px"></div>
  <div class="contact-item abs" style="left:823px">
    <svg width="18" height="14" viewBox="0 0 18 14"><rect width="18" height="14" rx="1.5" fill="#fff"/><path d="M1 1.5 L9 7.5 L17 1.5" stroke="#3dab6c" stroke-width="1.6" fill="none"/></svg>
    <span>post@kindlo-example.no</span>
  </div>
</section>

<footer class="site-footer abs"></footer>
<div class="partner-circle abs"></div>
<div class="partner-square abs"></div>

<h4 class="footer-heading abs" style="left:540px;top:2230px">Join Our Newsletter</h4>
<div class="field abs" style="top:2279px">Name</div>
<div class="field abs" style="top:2334px">Email</div>
<a class="btn subscribe abs" href="#">subscribe</a>

<h4 class="footer-heading abs" style="left:910px;top:2230px">Sitemap</h4>
<ul class="sitemap abs" style="left:910px">
  <li>&gt; Home</li><li>&gt; Program</li><li>&gt; Services</li><li>&gt; Support</li>
</ul>
<ul class="sitemap abs" style="left:1016px">
  <li>&gt; About</li><li>&gt; Privacy Policy</li><li>&gt; Contact</li>
</ul>

<div class="footer-rule abs"></div>
<p class="copyright abs">Copyright © 2017 Kindlo Norway. All Rights Reserved.</p>
<span class="social abs" style="left:952px"></span>
<span class="social abs" style="left:986px"></span>
<span class="social abs" style="left:1036px"></span>
<span class="social abs" style="left:1095px"></span>

</body>
</html>
```